Photobook template design

Just one book of 4/5 pages needed to find a handful of designers to help with this project that will be ongoing for several months, we will agree design price per book.

Hi there, we need lots of fabulous photobook templates designed:
there will be 20 books to start with, canvas layouts, calendar layouts etc.

The MAIN idea of the template is to facilitate the easiest creation / ordering of photobooks etc. possible for the client, so all they have to do is upload their pics and drop them into the templates you're going to design...

Each photobook needs to have min 20 pages, there can be a common theme throughout, but they must be different enough so that they do not all blend into one.
Choose to create a design from the following categories:
family
kids
travel
romance / love
seasonal holiday
year in review
everyday / general
recipes
pets / animals
collage
scrapbook

the quality and look and feel must be equal to www.pagerivo.example / www.snapduvel.example / www.framelyst.example.uk

In order to keep the designs as fresh as possible - we will work with several designers, so for this first project we will choose 1 designer, but then we'll create other design projects for which you will be specifically invited to design for - it's the only way the do multiple designs/projects.

please see 2 pics attached of other templates already designed - we're very happy with these...

Target Market(s)

These photobooks / calendars / canvas prints are for the average family - not too serious, must be fun / tongue in cheek etc.
They're for people who want to do photobooks but have no clue or do not have the time - so they must LOVE the design, and then want to just add their photos...

Industry/Entity Type

Travel

Requirements
Must have
• Must be designed in Indesign or Illustrator.
Metric sizes please - Either A3 landscape or portrait with 3 mm bleed, or 300 x 300mm square - 3mm bleed
If you place photos for proofing, please use imagorra images - we have a imagorra account

```html
<!DOCTYPE html>
<html lang="en">
<head>
<meta charset="utf-8">
<title>Smiles Scrapbook Template</title>
<link rel="stylesheet" href="https://fonts.googleapis.com/css2?family=Architects+Daughter&family=Nunito:wght@700;800&display=swap">
<style>
  :root {
    --paper: #efe4cc;
    --paper-dot-blue: #bfe0e4;
    --paper-dot-green: #d3e6b4;
    --band-green: #b9df7a;
    --band-dark: #3fa67c;
    --teal: #3cb5c8;
    --teal-deep: #2a96ad;
    --green: #93cd5e;
    --green-deep: #5fb356;
    --photo: #f6fafc;
    --sticker-yellow: #f1ef7a;
    --ink-teal: #2b8fb5;
    --white: #ffffff;
  }
  html, body {
    margin: 0;
    padding: 0;
    width: 1200px;
    height: 1000px;
    overflow: hidden;
    background: var(--white);
  }
  .template-board { display: block; width: 1200px; height: 1000px; }
  .photo-slot { fill: var(--photo); }
  .sticker-word {
    font-family: "Nunito", sans-serif;
    font-weight: 800;
    fill: var(--ink-teal);
  }
  .sticker-script {
    font-family: "Architects Daughter", cursive;
    fill: var(--sticker-yellow);
  }
</style>
</head>
<body>
<svg class="template-board" viewBox="0 0 1200 1000" xmlns="http://www.w3.org/2000/svg">
  <defs>
    <filter id="page-shadow" x="-5%" y="-5%" width="110%" height="115%">
      <feDropShadow dx="0" dy="4" stdDeviation="6" flood-color="#000" flood-opacity="0.25"/>
    </filter>
    <filter id="piece-shadow" x="-10%" y="-10%" width="125%" height="125%">
      <feDropShadow dx="2" dy="3" stdDeviation="3" flood-color="#000" flood-opacity="0.22"/>
    </filter>
    <linearGradient id="paper-fill" x1="0" y1="0" x2="1" y2="1">
      <stop offset="0" stop-color="#f1e6cf"/>
      <stop offset="0.5" stop-color="#e9e0c6"/>
      <stop offset="1" stop-color="#ede2c8"/>
    </linearGradient>
    <radialGradient id="halftone-fill" cx="0.5" cy="0.5" r="0.6">
      <stop offset="0" stop-color="#7fcf9a"/>
      <stop offset="0.6" stop-color="#3fb3c4"/>
      <stop offset="1" stop-color="#2b97b8"/>
    </radialGradient>
    <linearGradient id="stripe-fill" x1="0" y1="0" x2="0" y2="1">
      <stop offset="0" stop-color="#98cf63"/>
      <stop offset="0.3" stop-color="#5ebfae"/>
      <stop offset="0.55" stop-color="#8fcb63"/>
      <stop offset="0.8" stop-color="#4fb8c6"/>
      <stop offset="1" stop-color="#93cd5e"/>
    </linearGradient>
    <linearGradient id="plaid-fill" x1="0" y1="0" x2="1" y2="1">
      <stop offset="0" stop-color="#6fcbc9"/>
      <stop offset="1" stop-color="#3fa9c0"/>
    </linearGradient>
    <linearGradient id="smiles-fill" x1="0" y1="0" x2="0" y2="1">
      <stop offset="0" stop-color="#9ed05a"/>
      <stop offset="0.5" stop-color="#4fb3a8"/>
      <stop offset="1" stop-color="#2f8fa8"/>
    </linearGradient>
    <linearGradient id="band-fill" x1="0" y1="0" x2="1" y2="0">
      <stop offset="0" stop-color="#b6de77"/>
      <stop offset="0.5" stop-color="#c2e482"/>
      <stop offset="1" stop-color="#b2dc74"/>
    </linearGradient>
  </defs>

  <!-- Main spread page -->
  <g class="page page-main">
    <rect x="100" y="38" width="990" height="700" fill="url(#paper-fill)" filter="url(#page-shadow)"
          role="img" aria-label="Cream textured paper with soft blue and green polka dots"/>
    <g class="page-band">
      <rect x="100" y="535" width="990" height="84" fill="url(#band-fill)"/>
      <rect x="100" y="617" width="990" height="20" fill="var(--band-dark)"/>
    </g>

    <g class="frame-circle" filter="url(#piece-shadow)">
      <circle cx="470" cy="227" r="143" fill="url(#halftone-fill)" role="img" aria-label="Teal and green halftone paper circle"/>
    </g>
    <rect class="photo-slot" x="386" y="143" width="169" height="168"/>

    <g class="frame-oval" filter="url(#piece-shadow)">
      <ellipse cx="820" cy="418" rx="188" ry="260" fill="url(#stripe-fill)" role="img" aria-label="Green and teal striped paper oval"/>
    </g>
    <rect class="photo-slot" x="698" y="240" width="248" height="360"/>

    <g class="sticker-smiles" filter="url(#piece-shadow)" transform="rotate(8 939 149)">
      <path d="M885 95 Q939 80 993 95 Q1008 149 993 203 Q939 218 885 203 Q870 149 885 95 Z" fill="url(#smiles-fill)"/>
      <text class="sticker-script" x="942" y="132" font-size="16" text-anchor="middle">smiles</text>
      <text class="sticker-script" x="942" y="156" font-size="16" text-anchor="middle">smiles</text>
      <text class="sticker-script" x="942" y="180" font-size="16" text-anchor="middle">smiles</text>
    </g>

    <g class="sticker-plaid" filter="url(#piece-shadow)">
      <circle cx="236" cy="399" r="61" fill="url(#plaid-fill)" role="img" aria-label="Teal plaid paper circle"/>
    </g>
    <g class="sticker-laugh" filter="url(#piece-shadow)">
      <circle cx="181" cy="341" r="41" fill="var(--green)"/>
      <rect x="140" y="328" width="82" height="26" fill="#9fd6dc"/>
      <text class="sticker-word" x="181" y="349" font-size="19" text-anchor="middle">Laugh</text>
    </g>

    <rect class="photo-slot" x="176" y="458" width="327" height="219"/>
  </g>

  <!-- Thumbnail spread -->
  <g class="page page-thumb">
    <rect x="290" y="772" width="593" height="210" fill="url(#paper-fill)" filter="url(#page-shadow)"
          role="img" aria-label="Cream polka dot paper spread preview"/>
    <line x1="596" y1="772" x2="596" y2="982" stroke="#d9cfb5" stroke-width="1.5"/>
    <rect x="290" y="920" width="593" height="20" fill="url(#band-fill)"/>
    <rect x="290" y="939" width="593" height="5" fill="var(--band-dark)"/>

    <!-- left page -->
    <rect x="343" y="772" width="32" height="210" fill="var(--teal)" role="img" aria-label="Teal ric-rac ribbon"/>
    <g filter="url(#piece-shadow)">
      <rect x="318" y="795" width="60" height="63" fill="url(#smiles-fill)"/>
      <text class="sticker-word" x="348" y="823" font-size="13" text-anchor="middle" fill="#c8ee8a" style="fill:#c8ee8a">HAHA</text>
      <text class="sticker-word" x="348" y="843" font-size="13" text-anchor="middle" style="fill:#c8ee8a">HAHA</text>
    </g>
    <g filter="url(#piece-shadow)" transform="rotate(6 494 847)">
      <rect class="photo-slot" x="428" y="812" width="132" height="72"/>
    </g>
    <circle cx="537" cy="797" r="12" fill="var(--green)" filter="url(#piece-shadow)"/>
    <circle cx="494" cy="896" r="16" fill="var(--green-deep)"/>
    <rect class="photo-slot" x="303" y="915" width="47" height="47"/>
    <rect class="photo-slot" x="378" y="893" width="46" height="47"/>
    <rect class="photo-slot" x="435" y="912" width="47" height="47"/>
    <g filter="url(#piece-shadow)">
      <circle cx="535" cy="919" r="22" fill="var(--teal)"/>
      <text class="sticker-word" x="535" y="923" font-size="11" text-anchor="middle" style="fill:#dff4f4">LOL :)</text>
    </g>

    <!-- right page: miniature of main layout -->
    <circle cx="693" cy="824" r="38" fill="url(#halftone-fill)" filter="url(#piece-shadow)"/>
    <rect class="photo-slot" x="671" y="803" width="45" height="44"/>
    <ellipse cx="804" cy="884" rx="50" ry="77" fill="url(#stripe-fill)" filter="url(#piece-shadow)"/>
    <rect class="photo-slot" x="768" y="832" width="73" height="108"/>
    <path d="M822 793 Q838 788 854 793 Q858 808 854 823 Q838 828 822 823 Q818 808 822 793 Z" fill="url(#smiles-fill)" filter="url(#piece-shadow)"/>
    <circle cx="627" cy="884" r="17" fill="url(#plaid-fill)"/>
    <circle cx="611" cy="866" r="11" fill="var(--green)"/>
    <rect class="photo-slot" x="608" y="898" width="99" height="66"/>
  </g>
</svg>
</body>
</html>
```